Packaging Design Project - new spa massage oils brand

We need a packaging design for the products of a new line of oil for massage to be used at spas or by independent professionals. The brand name is "lumira", it's reminiscent of that ethereal moment where you lose track of the day-to-day and focus on yourself while being taken care off with aromatherapy, relaxing music and massage.
The packaging is a 250 ml transparent plastic bottle, the design will be in two labels, a front label with the brand and main design elements (product, net content, brand name) and a back label with more generic info. Both labels are of the same size 4.5 x 9 cm. A picture of the bottle will be provided in a separate file along with some ideas.
We are a start-up company in latin america, therefore the texts should be in spanish. There will be initially four SKU's, however, since we don't have a budget for all, we'll use the winning design and I'll use that as a base to create the other labels.
the four initial SKUs are:
-Rosemary (green pallet of colors)
-Lavender (purple pallet)
-Citrus (orange, yellow)
-Baby (pastels, predominantly blue)
We would expect you to focus on either the rosemary or lavender SKU's since those are our most important ones.
We don't have a logo yet for two reasons 1) budget constraints, 2) less restrictions for you to create the packaging artwork. If it's possible to add a mock-up of a logo it would be great.

the text for the back label (spanish) is:
Una combinación natural de aceites de semillas, flores y plantas para un masaje corporal relajante.
PRECAUCIONES: Mantener fuera del alcance de los niños. Evite el contacto con los ojos.
Este producto es biodegradable. No daña la capa de ozono.

translation (not to be on the lable, only for reference).
a combination of natural oils of seeds, flowers and plants for a relaxing body massage.
WARNING: keep out of reach of children, avoid eye contact.
this product is biodegradable. it doesn't damage the ozone layer.

Front label (spanish):
- lumira (this is the brand name)
- Aceite para masaje corporal con extracto de romero (this is the product description oil for body massage with rosemary extract)
- Frescura y vitalidad (this means freshness and vitality which are the characteristics of the rosemary oil)
- 250 ml (this is the net content)

Target Market(s)

consider that this product is used by professionals, however, the end consumers are mostly women (but not exclusive) of 30-45 years old.

Industry/Entity Type

Baby

Requirements
Nice to have
• -If the proposal could have a logo (even a simple one) it would be very much appreciated.
-Might want to try getting inspiration from other "ethereal" things such as smoke, watter ripples, air, fire, etc.
-A distinctive element of what the product has (for instance a picture or a sketch of a rosemary twig or a lavender flower).
-Colors are very important for these type of products, the whole pallet should be consistent. Consider that the rosemary oil is dark green, lavender is clear.
Should not have
• -Aggressive or excessively bright colors (this is a relaxation product).
-If you consider using a smoke texture, it should avoid dark, black shades that smoke usually evanesces into.
-Too polluted labels.

```html
<!DOCTYPE html>
<html lang="es">
<head>
<meta charset="utf-8">
<title>lumira Rosemary – etiquetas</title>
<link rel="stylesheet" href="https://fonts.googleapis.com/css2?family=Fira+Sans+Condensed:wght@400;600;700&family=Great+Vibes&display=swap">
<style>
  :root {
    --canvas: #f4f6f3;
    --label-white: #ffffff;
    --leaf: #1f9a4c;
    --leaf-deep: #17803d;
    --smoke-dark: #2f7f55;
    --smoke-mid: #6aa57a;
    --smoke-light: #cfe3d2;
    --text-green: #3a8f3c;
    --script-green: #86ad2c;
    --script-yellow: #d7e04a;
    --rule-yellow: #d9e05a;
    --ink-white: #ffffff;
  }
  * { margin: 0; padding: 0; box-sizing: border-box; }
  html, body { width: 753px; height: 1200px; overflow: hidden; }
  body {
    background: var(--canvas);
    font-family: "Fira Sans Condensed", "Arial Narrow", sans-serif;
    position: relative;
  }
  .label {
    position: absolute;
    top: 230px;
    width: 320px;
    height: 740px;
    overflow: hidden;
    text-align: center;
    box-shadow: 0 2px 10px rgba(0,0,0,0.08);
  }
  .label--front { left: 36px; background: var(--label-white); }
  .label--back { left: 397px; background: var(--leaf); }
  .abs { position: absolute; left: 0; width: 100%; }

  /* Front */
  .smoke-art {
    top: 0; height: 345px;
    background:
      radial-gradient(ellipse 60% 35% at 30% 25%, rgba(47,127,85,0.55), transparent 70%),
      radial-gradient(ellipse 70% 30% at 70% 65%, rgba(106,165,122,0.6), transparent 70%),
      radial-gradient(ellipse 50% 25% at 55% 45%, rgba(134,173,44,0.45), transparent 70%),
      linear-gradient(180deg, var(--smoke-mid) 0%, var(--smoke-light) 70%, var(--label-white) 100%);
  }
  .brand {
    font-weight: 600;
    letter-spacing: 0.5px;
    line-height: 1;
  }
  .label--front .brand { top: 105px; font-size: 56px; color: var(--ink-white); }
  .script {
    font-family: "Great Vibes", cursive;
    line-height: 1;
  }
  .label--front .script { top: 352px; font-size: 46px; color: var(--script-green); }
  .product-desc {
    top: 420px; font-size: 20px; font-weight: 700; line-height: 1.4;
    color: var(--text-green);
  }
  .divider {
    left: 50%; width: 9px; height: 9px; margin-left: -4.5px;
    border-radius: 50%;
  }
  .label--front .divider { background: var(--script-green); }
  .label--front .divider--one { top: 505px; }
  .label--front .divider--two { top: 588px; }
  .benefit { top: 535px; font-size: 19px; line-height: 1.2; color: var(--text-green); }
  .net-content { top: 618px; font-size: 19px; line-height: 1.2; color: var(--text-green); }
  .band { bottom: 0; height: 82px; }

  /* Back */
  .rule { height: 20px; }
  .rule--top { top: 24px; }
  .rule--bottom { top: 704px; }
  .label--back .brand { top: 70px; font-size: 60px; color: var(--ink-white); }
  .label--back .script { top: 150px; font-size: 46px; color: var(--script-yellow); }
  .blurb {
    top: 225px; font-size: 20px; font-weight: 700; line-height: 1.5;
    color: var(--ink-white);
  }
  .label--back .divider { background: var(--script-yellow); }
  .label--back .divider--one { top: 388px; }
  .label--back .divider--two { top: 662px; }
  .precautions {
    top: 425px; font-size: 19px; line-height: 1.55; color: var(--ink-white);
  }
  .eco-note {
    top: 572px; font-size: 19px; line-height: 1.55; color: var(--ink-white);
  }
</style>
</head>
<body>

<section class="label label--front">
  <div class="abs smoke-art" role="img" aria-label="Humo verde etéreo que se disuelve en blanco"></div>
  <div class="abs brand">lumira</div>
  <div class="abs script">Rosemary</div>
  <p class="abs product-desc">Aceite para masaje corporal<br>con extracto de romero</p>
  <span class="abs divider divider--one"></span>
  <p class="abs benefit">Frescura y vitalidad</p>
  <span class="abs divider divider--two"></span>
  <p class="abs net-content">250 ml</p>
  <svg class="abs band" viewBox="0 0 320 82" preserveAspectRatio="none" aria-hidden="true">
    <path d="M0 0 Q160 50 320 0 L320 82 L0 82 Z" fill="var(--leaf)"/>
    <path d="M0 28 Q160 78 320 28" fill="none" stroke="var(--label-white)" stroke-width="2.5"/>
  </svg>
</section>

<section class="label label--back">
  <svg class="abs rule rule--top" viewBox="0 0 320 20" preserveAspectRatio="none" aria-hidden="true">
    <path d="M0 14 Q160 4 320 14" fill="none" stroke="var(--rule-yellow)" stroke-width="2"/>
  </svg>
  <div class="abs brand">lumira</div>
  <div class="abs script">Rosemary</div>
  <p class="abs blurb">Una combinación natural<br>de aceites de semillas,<br>flores y plantas para<br>un masaje corporal relajante.</p>
  <span class="abs divider divider--one"></span>
  <p class="abs precautions">PRECAUCIONES:<br>Mantener fuera del<br>alcance de los niños.<br>Evite el contacto con los ojos.</p>
  <p class="abs eco-note">Este producto es biodegradable.<br>No daña la capa de ozono.</p>
  <span class="abs divider divider--two"></span>
  <svg class="abs rule rule--bottom" viewBox="0 0 320 20" preserveAspectRatio="none" aria-hidden="true">
    <path d="M0 4 Q160 14 320 4" fill="none" stroke="var(--rule-yellow)" stroke-width="2"/>
  </svg>
</section>

</body>
</html>
```